Piano genealogy graphs template, for a large poster printing

Hello and thank you for your interest in my project.
I need a poster template, so I can create structures similar to the one I have uploaded. I want to completely replace or improve my poor previous design which is attached.
I need to be able to input names and dates into boxes of various colors, arrows pointing between boxes. I would also like to be able to label each graph (not each box).
I am looking at something that would be legible when printed, in a one consistent professional layout of 2A0 (around 1189x1682 mm) poster (I know it is large). The design template required here can include just few sample text boxes with sample flags on a suitable background, for me to multiply later and spread across the whole poster.
The positioning of the boxes is not important.
Please let me know if more clarification is required.
Thank you for your help.

Feel free to follow what I have attached in the file, or change the design completely.

UPDATE 4/12: I have uploaded two more graphs as an example. At this stage of the contest, I would like to have one of those graphs done, and I am planning to offer a 'freelance job' to one or two designers, who will be willing to do the whole 10 graphs on one poster.
Updates

Reason: Dear Designers, Since the project is rather complex and large-scale, I have decided to give everyone more time to work on their designs. I will consider extending it further if any of you require additional time. Best wishes, bronisław

Dear Designers, I would like to inform you that the contest for my poster is now closed and that I have assigned the prizes. I would like to thank all of you for submiting your high-quality designs, and for your participation. It was a great pleasure working with all of you. Due to the large size of the project itself (large number of graphs to be fitted on a single poster), I had to focus on providing feedback to only those designers who provided projects closest to what I was expecting at the early stages of the contest. I wish you all the best for the future, Kind regards, Bronisław

Target Market(s)

Pianists, historians

Industry/Entity Type

Printing

Requirements
Must have
• Consistent design, but allow to clearly delineate various genealogy trees.

```html
<!DOCTYPE html>
<html lang="en">
<head>
<meta charset="utf-8">
<title>Genealogical Trees of Pianists – French Tree</title>
<link href="https://fonts.googleapis.com/css2?family=Montserrat:wght@800;900&family=Open+Sans:ital,wght@0,400;0,600;1,700;1,800&display=swap" rel="stylesheet">
<style>
:root{
  --red:#e41f2d;
  --ink:#1f1f21;
  --white:#ffffff;
  --page:#ececec;
  --line:#bdbdbd;
  --flag-blue:#1f3f9a;
  --flag-red:#e3262f;
}
*{box-sizing:border-box;margin:0;padding:0}
html,body{width:1200px;height:1000px;overflow:hidden;background:var(--page)}
.poster{
  position:absolute;left:257px;top:16px;width:596px;height:842px;
  transform:scale(1.15);transform-origin:0 0;
  background:linear-gradient(180deg,#f4f4f4 0%,#ffffff 18%,#ffffff 70%,#d6d6d6 100%);
  overflow:hidden;font-family:"Open Sans",Arial,sans-serif;
}
.kicker{
  position:absolute;left:0;right:0;top:40px;text-align:center;
  font-family:"Montserrat",Arial,sans-serif;font-weight:900;font-size:15.5px;color:var(--red);letter-spacing:.2px;
}
.title-plate{
  position:absolute;left:122px;top:65px;width:352px;height:65px;background:var(--red);border-radius:12px;
}
.title-plate::before{
  content:"";position:absolute;inset:5px;border:2px solid var(--white);border-radius:8px;
}
.title-plate h1{
  position:absolute;inset:0;display:flex;align-items:center;justify-content:center;
  font-family:"Montserrat",Arial,sans-serif;font-weight:900;font-size:52px;color:var(--white);letter-spacing:2px;
}
.branch-head{position:absolute;left:0;top:140px;width:596px;height:100px}
.piano-icon{position:absolute;left:306px;top:38px;width:30px;height:26px;background:var(--white);border-radius:3px 10px 3px 3px}
.music-motif{
  position:absolute;left:30px;top:560px;width:540px;height:270px;
  background:radial-gradient(ellipse at 30% 60%,rgba(150,150,150,.22),rgba(150,150,150,0) 65%);
}
.links{position:absolute;left:0;top:0;width:596px;height:842px}
.card{
  position:absolute;background:var(--ink);color:var(--white);
  border-radius:2px 14px 2px 14px;padding:5px 7px 4px 7px;
}
.card-head{display:flex;align-items:center;gap:5px;font-style:italic;font-weight:800;font-size:6.2px;line-height:8px}
.card-head.solo{height:100%}
.flag{display:inline-block;width:10px;height:7px;flex:none;
  background:linear-gradient(90deg,var(--flag-blue) 0 33.3%,var(--white) 33.3% 66.6%,var(--flag-red) 66.6%)}
.label{font-size:3.6px;font-weight:700;letter-spacing:.3px;margin:1px 0 1px 15px}
.students{list-style:none}
.students li{display:flex;align-items:center;gap:5px;font-size:5.4px;line-height:7.1px}
.students li::before{content:"";width:6px;height:4.5px;flex:none;
  background:linear-gradient(90deg,var(--flag-blue) 0 33.3%,var(--white) 33.3% 66.6%,var(--flag-red) 66.6%)}
.students li span{color:#cfcfcf;margin-left:2px}
</style>
</head>
<body>
<main class="poster">
  <p class="kicker">GENEALOGICAL TREES OF</p>
  <div class="title-plate"><h1>PIANISTS</h1></div>

  <div class="branch-head">
    <svg width="596" height="100" viewBox="0 0 596 100">
      <path d="M40 18 H270 L282 48 L270 78 H40 Z" fill="var(--red)"/>
      <path d="M288 18 H346 L360 48 L346 78 H288 L300 48 Z" fill="var(--red)"/>
      <line x1="372" y1="55" x2="596" y2="55" stroke="var(--red)" stroke-width="1.2"/>
      <circle cx="54" cy="48" r="31" fill="var(--white)" stroke="var(--red)" stroke-width="4"/>
      <circle cx="54" cy="48" r="24" fill="none" stroke="var(--red)" stroke-width="1.5"/>
      <defs><path id="arc" d="M34 46 A20 20 0 0 1 74 46"/></defs>
      <text font-family="Montserrat,Arial,sans-serif" font-weight="900" font-size="8" fill="var(--red)" letter-spacing="1">
        <textPath href="#arc" startOffset="50%" text-anchor="middle">BRANCH</textPath></text>
      <text x="54" y="70" text-anchor="middle" font-family="Montserrat,Arial,sans-serif" font-weight="900" font-size="30" fill="var(--red)">1</text>
      <text x="96" y="56" font-family="Montserrat,Arial,sans-serif" font-weight="800" font-size="21" fill="var(--white)">French Tree</text>
    </svg>
    <div class="piano-icon" role="img" aria-label="Grand piano icon"></div>
  </div>

  <div class="music-motif" role="img" aria-label="Faint treble clef and flowing music notes decoration"></div>

  <svg class="links" viewBox="0 0 596 842" fill="none" stroke="var(--line)" stroke-width=".8">
    <path d="M83 304V316 M223 304V316 M365 304V316 M509 304V316 M83 316H509 M226 316V338"/>
    <path d="M214 360V405 M151 430H180V440H211 M365 385V398H300V405 M509 385V410H466V420"/>
    <path d="M274 495V523 M403 490H370V560H338 M150 530H180V555H211"/>
    <path d="M274 613V640 M112 625H417 M112 612V625 M417 612V625 M274 666V690"/>
    <g fill="var(--red)" stroke="none">
      <circle cx="226" cy="316" r="1.6"/><circle cx="365" cy="316" r="1.6"/><circle cx="180" cy="440" r="1.6"/>
      <circle cx="300" cy="398" r="1.6"/><circle cx="466" cy="410" r="1.6"/><circle cx="370" cy="525" r="1.6"/>
      <circle cx="180" cy="555" r="1.6"/><circle cx="274" cy="625" r="1.6"/><circle cx="112" cy="625" r="1.6"/>
      <circle cx="417" cy="625" r="1.6"/><circle cx="274" cy="680" r="1.6"/><circle cx="214" cy="380" r="1.6"/>
    </g>
  </svg>

  <!-- row one -->
  <section class="card" style="left:21px;top:260px;width:125px;height:44px">
    <h2 class="card-head"><i class="flag"></i>Henri Valmont (1916-2008)</h2>
    <p class="label">STUDENTS:</p>
    <ul class="students" style="margin-left:9px"><li>Jean-Marc Dorval<span>(1948)</span></li><li>Jacques Fontanel<span>(1947)</span></li><li>Jean-Luc Morvan<span>(1944)</span></li></ul>
  </section>
  <section class="card" style="left:161px;top:260px;width:125px;height:50px">
    <h2 class="card-head"><i class="flag"></i>Odette Marsan (1906)</h2>
    <p class="label">STUDENTS:</p>
    <ul class="students" style="margin-left:9px"><li>Jean-Rémi Castagne<span>(1961)</span></li><li>Mireille Sautet<span>(1952)</span></li><li>Pascal Verdier<span>(1951)</span></li><li>Clara Sautet<span>(1950)</span></li></ul>
  </section>
  <section class="card" style="left:301px;top:260px;width:129px;height:50px">
    <h2 class="card-head"><i class="flag"></i>Jules Aubrac (1907-1982)</h2>
    <p class="label">STUDENTS:</p>
    <ul class="students" style="margin-left:9px"><li>Ilse Baran<span>(1941)</span></li><li>Mireille Sautet<span>(1940)</span></li><li>Dominique Favre<span>(1938)</span></li><li>Philippe Arnaud<span>(1934)</span></li></ul>
  </section>
  <section class="card" style="left:445px;top:260px;width:128px;height:56px">
    <h2 class="card-head"><i class="flag"></i>Hélène Varenne (1924-2010)</h2>
    <p class="label">STUDENTS:</p>
    <ul class="students" style="margin-left:9px"><li>Nicolas Andrel<span>(1970)</span></li><li>Pierre-Louis Armand<span>(1957)</span></li><li>Peter Dunmore<span>(1953)</span></li><li>Michel Bardin<span>(1950)</span></li><li>Paul Cresswell<span>(1944)</span></li></ul>
  </section>

  <!-- row two -->
  <section class="card" style="left:21px;top:335px;width:130px;height:130px">
    <h2 class="card-head"><i class="flag"></i>Hélène Varenne (1924-2010)</h2>
    <p class="label">STUDENTS:</p>
    <ul class="students" style="margin-left:9px"><li>Nicolas Andrel<span>(1970)</span></li><li>Pierre-Louis Armand<span>(1957)</span></li><li>Peter Dunmore<span>(1953)</span></li><li>Michel Bardin<span>(1950)</span></li><li>Paul Cresswell<span>(1944)</span></li><li>Jean-Marc Dorval<span>(1948)</span></li><li>Jacques Fontanel<span>(1947)</span></li><li>Jean-Luc Morvan<span>(1944)</span></li><li>Jean-Rémi Castagne<span>(1961)</span></li><li>Mireille Sautet<span>(1952)</span></li><li>Pascal Verdier<span>(1951)</span></li><li>Clara Sautet<span>(1950)</span></li><li>Peter Dunmore<span>(1953)</span></li><li>Michel Bardin<span>(1950)</span></li><li>Mireille Sautet<span>(1952)</span></li></ul>
  </section>
  <section class="card" style="left:163px;top:338px;width:103px;height:22px;padding-top:0;padding-bottom:0">
    <h2 class="card-head solo"><i class="flag"></i>Louis Brevan (1890-1956)</h2>
  </section>
  <section class="card" style="left:301px;top:338px;width:129px;height:47px">
    <h2 class="card-head"><i class="flag"></i>Odette Marsan (1906)</h2>
    <p class="label">STUDENTS:</p>
    <ul class="students" style="margin-left:9px"><li>Jean-Rémi Castagne<span>(1961)</span></li><li>Mireille Sautet<span>(1952)</span></li><li>Pascal Verdier<span>(1951)</span></li><li>Clara Sautet<span>(1950)</span></li></ul>
  </section>
  <section class="card" style="left:445px;top:338px;width:128px;height:47px">
    <h2 class="card-head"><i class="flag"></i>Odette Marsan (1906)</h2>
    <p class="label">STUDENTS:</p>
    <ul class="students" style="margin-left:9px"><li>Jean-Rémi Castagne<span>(1961)</span></li><li>Mireille Sautet<span>(1952)</span></li><li>Pascal Verdier<span>(1951)</span></li><li>Clara Sautet<span>(1950)</span></li></ul>
  </section>

  <!-- middle -->
  <section class="card" style="left:211px;top:405px;width:127px;height:90px">
    <h2 class="card-head"><i class="flag"></i>Hélène Varenne (1924-2010)</h2>
    <p class="label">STUDENTS:</p>
    <ul class="students" style="margin-left:9px"><li>Nicolas Andrel<span>(1970)</span></li><li>Pierre-Louis Armand<span>(1957)</span></li><li>Peter Dunmore<span>(1953)</span></li><li>Michel Bardin<span>(1950)</span></li><li>Paul Cresswell<span>(1944)</span></li><li>Jean-Marc Dorval<span>(1948)</span></li><li>Jacques Fontanel<span>(1947)</span></li><li>Jean-Luc Morvan<span>(1944)</span></li><li>Jean-Rémi Castagne<span>(1961)</span></li><li>Mireille Sautet<span>(1952)</span></li></ul>
  </section>
  <section class="card" style="left:403px;top:420px;width:127px;height:130px">
    <h2 class="card-head"><i class="flag"></i>Hélène Varenne (1924-2010)</h2>
    <p class="label">STUDENTS:</p>
    <ul class="students" style="margin-left:9px"><li>Nicolas Andrel<span>(1970)</span></li><li>Pierre-Louis Armand<span>(1957)</span></li><li>Peter Dunmore<span>(1953)</span></li><li>Michel Bardin<span>(1950)</span></li><li>Paul Cresswell<span>(1944)</span></li><li>Jean-Marc Dorval<span>(1948)</span></li><li>Jacques Fontanel<span>(1947)</span></li><li>Jean-Luc Morvan<span>(1944)</span></li><li>Jean-Rémi Castagne<span>(1961)</span></li><li>Mireille Sautet<span>(1952)</span></li><li>Pascal Verdier<span>(1951)</span></li><li>Clara Sautet<span>(1950)</span></li><li>Peter Dunmore<span>(1953)</span></li><li>Michel Bardin<span>(1950)</span></li><li>Mireille Sautet<span>(1952)</span></li></ul>
  </section>
  <section class="card" style="left:21px;top:498px;width:129px;height:59px">
    <h2 class="card-head"><i class="flag"></i>Hélène Varenne (1924-2010)</h2>
    <p class="label">STUDENTS:</p>
    <ul class="students" style="margin-left:9px"><li>Nicolas Andrel<span>(1970)</span></li><li>Pierre-Louis Armand<span>(1957)</span></li><li>Peter Dunmore<span>(1953)</span></li><li>Michel Bardin<span>(1950)</span></li><li>Paul Cresswell<span>(1944)</span></li></ul>
  </section>
  <section class="card" style="left:211px;top:523px;width:127px;height:90px">
    <h2 class="card-head"><i class="flag"></i>Hélène Varenne (1924-2010)</h2>
    <p class="label">STUDENTS:</p>
    <ul class="students" style="margin-left:9px"><li>Nicolas Andrel<span>(1970)</span></li><li>Pierre-Louis Armand<span>(1957)</span></li><li>Peter Dunmore<span>(1953)</span></li><li>Michel Bardin<span>(1950)</span></li><li>Paul Cresswell<span>(1944)</span></li><li>Jean-Marc Dorval<span>(1948)</span></li><li>Jacques Fontanel<span>(1947)</span></li><li>Jean-Luc Morvan<span>(1944)</span></li><li>Jean-Rémi Castagne<span>(1961)</span></li><li>Mireille Sautet<span>(1952)</span></li></ul>
  </section>

  <!-- roots -->
  <section class="card" style="left:60px;top:590px;width:105px;height:22px;padding-top:0;padding-bottom:0">
    <h2 class="card-head solo"><i class="flag"></i>Louis Brevan (1890-1956)</h2>
  </section>
  <section class="card" style="left:366px;top:590px;width:102px;height:22px;padding-top:0;padding-bottom:0">
    <h2 class="card-head solo"><i class="flag"></i>Louis Brevan (1890-1956)</h2>
  </section>
  <section class="card" style="left:213px;top:640px;width:125px;height:26px;padding-top:0;padding-bottom:0">
    <h2 class="card-head solo"><i class="flag"></i>Louis Brevan (1890-1956)</h2>
  </section>
  <section class="card" style="left:213px;top:690px;width:125px;height:26px;padding-top:0;padding-bottom:0">
    <h2 class="card-head solo"><i class="flag"></i>Louis Brevan (1890-1956)</h2>
  </section>
</main>
</body>
</html>
```